Suds Harbor Laundromat Wordpress Design

We need a Wordpress website design for our laundromat, Suds Harbor Atlanta, at www.sudsharboratlanta-example.com. We would like to have 6 pages: Home, About Us, Services, Locations, Reviews and Contact us. We will provide content for the text on each page. What we do: We are a full service laundromat that provides dry cleaning drop off, professional laundry services, wash dry fold and self service laundry to the local community. We would like to use the color scheme from our logo to convey a warm, safe, and bright business that caters to its diverse community.
Updates

I like the structure of this laundromat website: http://www.tumblewashhub-example.com/ Using my logo and color scheme in the above referenced website is what. Am looking for. The photos attached to the project with the female model should be used as a primary focus and supplemented by actual photos of the equipment.

Target Market(s)

Our target market is a diverse group of people from Midtown Atlanta - LGBTQ community /Locals/Regulars that have been coming to laundromat for 30 years.

Industry/Entity Type

Laundromat

Coding

Coded - Design and coding required

Number of Pages Required

5+ page

Font styles to use
Sans Serif

Colors
0054AA
0677BA
7BADD7
CADEEF
E8F1F8

Requirements
Must have
• Feature this video on the main page: https://video.example.com/Qx7mBr2Lp0Z

```html
<!DOCTYPE html>
<html lang="en">
<head>
<meta charset="utf-8">
<title>Suds Harbor Laundromat</title>
<link rel="stylesheet" href="https://fonts.googleapis.com/css2?family=Bebas+Neue&family=Open+Sans:wght@400;600;700&display=swap">
<style>
:root{
  --navy:#1d5ea8;
  --blue:#0677ba;
  --sky:#1e9ad8;
  --light:#7badd7;
  --pale:#cadeef;
  --mist:#e8f1f8;
  --ink:#333;
  --muted:#777;
  --white:#fff;
  --gold:#f2b01e;
}
*{box-sizing:border-box;margin:0;padding:0}
html,body{width:1200px;height:4164px;overflow:hidden}
body{position:relative;background:var(--white);font-family:'Open Sans',sans-serif;color:var(--ink)}
.abs{position:absolute}
.display{font-family:'Bebas Neue',sans-serif;letter-spacing:1px;font-weight:400}
.section-title{position:absolute;left:0;width:1200px;text-align:center;font-size:40px;color:#2a2a2a;line-height:1.1}

/* header */
.brand{left:105px;top:36px;font-size:40px;color:var(--navy);line-height:1}
.brand-sub{left:105px;top:80px;font-size:13px;color:var(--sky);letter-spacing:.5px}
.brand-dot{left:238px;top:22px;width:14px;height:14px;border-radius:50%;background:var(--sky)}
.contact-chip{top:56px;display:flex;align-items:center;gap:12px}
.chip-icon{width:40px;height:40px;border-radius:50%;background:var(--navy);display:flex;align-items:center;justify-content:center}
.chip-label{font-family:'Bebas Neue',sans-serif;color:var(--navy);font-size:14px;line-height:1}
.chip-value{font-size:14px;color:#444}

/* nav */
.nav{left:0;top:142px;width:1200px;height:57px;background:var(--navy);display:flex;padding-left:105px}
.nav a{width:180px;color:var(--white);text-decoration:none;font-size:16px;display:flex;align-items:center;justify-content:center;position:relative}
.nav a:first-child{width:146px;background:var(--sky)}
.nav a+a:not(:nth-child(2))::before{content:"";position:absolute;left:0;top:20px;height:18px;border-left:1px solid rgba(255,255,255,.35)}

/* hero */
.hero{left:0;top:199px;width:1200px;height:660px;
  background:
    linear-gradient(180deg,rgba(120,140,135,.55) 0%,rgba(120,140,135,0) 22%,rgba(0,0,0,0) 75%,rgba(90,95,95,.35) 100%),
    linear-gradient(90deg,#7f8d93 0%,#b9bab2 10%,#d8d3c1 24%,#dcd7c5 45%,#cfcab8 58%,#7aa2cf 66%,#2f74c2 70%,#6f98c6 75%,#d3cebc 82%,#c9c4b2 92%,#9ea5a3 100%)}
.hero-caption{left:105px;top:417px;width:388px;height:160px;background:var(--sky);clip-path:polygon(0 0,100% 0,78% 100%,0 100%);padding:30px 26px;color:var(--white)}
.hero-caption h1{font-size:34px;line-height:1}
.hero-caption p{font-size:14px;margin-top:18px;line-height:1.2;width:300px}
.hero-arrow{top:695px;width:38px;height:38px;border-radius:50%;background:var(--sky);display:flex;align-items:center;justify-content:center}

/* about */
.about-photo{left:89px;top:1040px;width:538px;height:444px}
.about-heading{left:639px;top:1060px;font-size:17px;color:var(--navy)}
.about-rule{left:639px;top:1096px;width:90px;height:2px;background:var(--navy)}
.about-copy{left:642px;top:1116px;width:452px;font-size:12.5px;line-height:1.45;color:#666}
.about-copy p{margin-bottom:16px}
.pill{height:50px;border-radius:25px;background:var(--navy);color:var(--white);display:flex;align-items:center;justify-content:space-between;font-size:16px;padding:0 10px 0 28px;white-space:nowrap}
.pill i{flex:none;width:30px;height:30px;border-radius:50%;background:var(--white);display:flex;align-items:center;justify-content:center}

/* services */
.service-band{left:0;top:1887px;width:1200px;height:672px;background:linear-gradient(180deg,#1a8fd0 0%,#2aa3e0 100%)}
.card{top:1659px;width:312px;height:436px;background:var(--white);border-radius:8px;box-shadow:0 4px 14px rgba(0,0,0,.12);overflow:hidden;text-align:center}
.card-photo{height:228px}
.card-badge{position:absolute;left:130px;top:200px;width:54px;height:54px;border-radius:50%;background:var(--white);display:flex;align-items:center;justify-content:center}
.card h3{margin-top:40px;font-size:22px;color:#2a2a2a}
.card p{margin:18px auto 0;width:262px;font-size:13px;line-height:1.35;color:#888}
.card .go{margin-top:18px}
.feature{top:2228px;width:166px;text-align:center;color:var(--white)}
.feature-ring{width:166px;height:166px;border-radius:50%;background:var(--white);display:flex;align-items:center;justify-content:center}
.feature h4{margin-top:20px;font-size:19px;line-height:1}
.feature p{font-size:13px;line-height:1.35;margin-top:4px}

/* testimonials */
.review{top:2768px;width:312px;height:312px;border-radius:50%;background:var(--navy);color:var(--white);text-align:center}
.review-avatar{position:absolute;left:-4px;top:-10px;width:104px;height:104px;border-radius:50%;border:6px solid var(--white);background:linear-gradient(160deg,#d7d3cf,#7f8790)}
.review-quote{position:absolute;left:148px;top:30px;font-family:Georgia,serif;font-size:60px;line-height:1;font-weight:700}
.review h5{margin-top:106px;font-size:13px;font-weight:700}
.review .role{font-size:12.5px}
.review p{width:250px;margin:18px auto 0;font-size:12.5px;line-height:1.35}
.stars{margin-top:24px;color:var(--gold);font-size:15px;letter-spacing:3px}
.dots{left:578px;top:3116px;display:flex;gap:5px}
.dots span{width:9px;height:9px;border-radius:50%;background:var(--navy)}
.dots span:first-child{background:var(--white);border:1.5px solid var(--navy)}

/* contact */
.qc-title{left:105px;top:3245px;font-size:42px;color:#2a2a2a}
.qc-sub{left:108px;top:3292px;font-size:14px;color:#555}
.field{background:#f3f3f3;height:38px;font-size:14px;color:#555;padding:9px 10px}
.send{left:108px;top:3501px;width:154px;height:39px;border-radius:20px;background:var(--navy);color:var(--white);font-size:14px;display:flex;align-items:center;justify-content:center}
.qc-photo{left:624px;top:3223px;width:471px;height:355px;border-radius:6px;background:linear-gradient(110deg,#a9b4b5 0%,#cfd3cc 45%,#7c3b23 60%,#2f6fb3 85%);box-shadow:0 4px 14px rgba(0,0,0,.15)}

/* footer */
.footer-wave{left:0;top:3640px;width:1200px;height:460px}
.f-head{top:3801px;font-size:15px;font-weight:700;color:var(--white)}
.f-head::after{content:"";display:block;width:44px;height:2px;background:var(--sky);margin-top:6px}
.f-map{left:105px;top:3855px;width:238px;height:155px;border:4px solid var(--white);background:linear-gradient(135deg,#d9e6cf,#eef0e6 50%,#cfe0ea)}
.f-links{left:438px;top:3862px;list-style:none;font-size:12px;color:var(--white)}
.f-links li{height:27px}
.f-links li::before{content:"→";margin-right:10px}
.f-text{font-size:12px;color:var(--white);line-height:1.85}
.f-input{left:898px;top:3927px;width:197px;height:31px;border-radius:16px;background:var(--white);font-size:12px;color:#666;padding:7px 14px}
.f-btn{left:898px;top:3974px;width:197px;height:31px;border-radius:16px;background:var(--sky);font-size:12px;color:var(--white);text-align:center;padding-top:7px}
.copyright{left:105px;top:4113px;font-size:12px;color:#444}
.copyright b{color:var(--navy);font-weight:600}
.social{top:4104px;width:34px;height:34px;border-radius:50%;background:var(--sky)}
</style>
</head>
<body>

<!-- header -->
<div class="abs brand-dot"></div>
<div class="abs brand display">Suds Harbor</div>
<div class="abs brand-sub">A FULL SERVICE LAUNDROMAT</div>

<div class="abs contact-chip" style="left:728px">
  <div class="chip-icon"><svg width="18" height="18" viewBox="0 0 24 24" fill="#fff"><path d="M6.6 10.8a15 15 0 0 0 6.6 6.6l2.2-2.2c.3-.3.7-.4 1-.2 1.1.4 2.3.6 3.6.6.6 0 1 .4 1 1V20c0 .6-.4 1-1 1A17 17 0 0 1 3 4c0-.6.4-1 1-1h3.5c.6 0 1 .4 1 1 0 1.3.2 2.5.6 3.6.1.3 0 .7-.2 1z"/></svg></div>
  <div><div class="chip-label">CALL US</div><div class="chip-value">(404) 555-0182</div></div>
</div>
<div class="abs contact-chip" style="left:888px">
  <div class="chip-icon"><svg width="18" height="18" viewBox="0 0 24 24" fill="#fff"><path d="M3 5h18v14H3z M3 5l9 7 9-7" stroke="#1d5ea8" stroke-width="1.5"/></svg></div>
  <div><div class="chip-label">EMAIL US</div><div class="chip-value">hello@sudsharbor-example.com</div></div>
</div>

<nav class="abs nav">
  <a>Home</a><a>About us</a><a>Servicese</a><a>Locationse</a><a>Reviewse</a><a>Contact Us</a>
</nav>

<!-- hero -->
<div class="abs hero" role="img" aria-label="Woman in a blue dress walking past a row of front-load washers in the laundromat"></div>
<svg class="abs" style="left:0;top:740px" width="1200" height="125" viewBox="0 0 1200 125">
  <path d="M0 55 C180 10 330 25 520 70 C700 110 900 95 1200 20 L1200 125 L0 125Z" fill="#fff"/>
  <path d="M0 55 C180 10 330 25 520 70 C700 110 900 95 1200 20 L1200 40 C900 110 700 120 520 84 C330 44 180 28 0 72Z" fill="#1e9ad8"/>
</svg>
<div class="abs hero-caption">
  <h1 class="display">RIGHT CLEANING</h1>
  <p>Located conveniently in Midtown next to Harbor Street Market In The Maple Court Shopping Center</p>
</div>
<div class="abs hero-arrow" style="left:105px"><svg width="16" height="16" viewBox="0 0 16 16"><path d="M13 8H3M7 4 3 8l4 4" stroke="#fff" stroke-width="1.8" fill="none"/></svg></div>
<div class="abs hero-arrow" style="left:155px"><svg width="16" height="16" viewBox="0 0 16 16"><path d="M3 8h10M9 4l4 4-4 4" stroke="#fff" stroke-width="1.8" fill="none"/></svg></div>

<!-- about -->
<h2 class="section-title display" style="top:958px">ABOUT US</h2>
<svg class="abs about-photo" viewBox="0 0 538 444">
  <defs>
    <linearGradient id="aboutTone" x1="0" y1="0" x2="0" y2="1">
      <stop offset="0" stop-color="#8fa9a7"/>
      <stop offset=".45" stop-color="#a3b3b0"/>
      <stop offset=".55" stop-color="#cfcfc8"/>
      <stop offset=".8" stop-color="#b4b4ad"/>
      <stop offset="1" stop-color="#6d7275"/>
    </linearGradient>
  </defs>
  <path d="M300 20 C360 -12 450 10 470 90 L480 190 L400 190Z" fill="#1d5ea8"/>
  <path d="M170 380 C220 450 350 455 400 395Z" fill="#1d5ea8"/>
  <path d="M30 150 C0 210 -5 280 15 320 L60 300 L70 140Z" fill="#1d5ea8"/>
  <path d="M60 80 C120 30 250 10 330 35 C420 62 470 130 470 200 L470 370 C430 405 300 395 200 392 C110 390 20 405 5 330 C-5 250 20 130 60 80Z" fill="url(#aboutTone)" role="img" aria-label="Laundromat interior with retro shop sign above a row of washers"/>
  <circle cx="472" cy="178" r="68" fill="#1e9ad8"/>
  <text x="472" y="178" text-anchor="middle" font-family="Bebas Neue, sans-serif" font-size="30" fill="#fff">45 YEARS</text>
  <text x="472" y="200" text-anchor="middle" font-family="Bebas Neue, sans-serif" font-size="17" letter-spacing="2" fill="#fff">EXPERIENCE</text>
</svg>
<div class="abs about-heading">WELCOME TO SUDS HARBOR</div>
<div class="abs about-rule"></div>
<div class="abs about-copy">
  <p>Lorem Ipsum is simply dummy text of the printing and typesetting industry has been the industry's standard dummy text ever since the 1500s,</p>
  <p>when an unknown printer took a galley of type and scrambled it to make a type specimen book. It has survived not only five centuries, but also the leap into electronic typesetting, remaining essentially unchanged. It was popularised in the 1960s</p>
  <p>with the release of LetterSet sheets containing Lorem Ipsum passages, and more recently with desktop publishing software like PageBuilder Pro includinginto electronic typesetting, remaining essentially unchanged. It was popularised versions of Lorem Ipsum.</p>
  <p>Lorem Ipsum is simply dummy text of the printing and typesetting industry has been the industry's standard dummy text ever since the 1500s.</p>
</div>
<div class="abs pill" style="left:639px;top:1409px;width:163px">Read More <i><svg width="14" height="14" viewBox="0 0 16 16"><path d="M3 8h10M9 4l4 4-4 4" stroke="#1d5ea8" stroke-width="2" fill="none"/></svg></i></div>

<!-- services -->
<h2 class="section-title display" style="top:1573px">OUR SERVICES</h2>
<div class="abs service-band"></div>

<div class="abs card" style="left:105px">
  <div class="card-photo" style="background:linear-gradient(135deg,#6b6f72,#c9ccce)" role="img" aria-label="Hand inserting a coin into a washer slot"></div>
  <div class="card-badge"><svg width="30" height="30" viewBox="0 0 30 30" fill="none" stroke="#1d5ea8" stroke-width="1.5"><rect x="6" y="3" width="18" height="24" rx="2"/><circle cx="15" cy="17" r="6"/><line x1="9" y1="8" x2="14" y2="8"/></svg></div>
  <h3 class="display">COIN LAUNDRY</h3>
  <p>Lorem Ipsum is simply dummy text of the printing and typesetting industry has been the industry's standard dummy.</p>
  <div class="go"><svg width="34" height="12" viewBox="0 0 34 12"><path d="M0 6h32M27 1l5 5-5 5" stroke="#1d5ea8" stroke-width="1.5" fill="none"/></svg></div>
</div>
<div class="abs card" style="left:445px">
  <div class="card-photo" style="background:linear-gradient(135deg,#9cb7de,#eef1f4)" role="img" aria-label="Woman steaming a blue shirt on a hanger"></div>
  <div class="card-badge"><svg width="30" height="30" viewBox="0 0 30 30" fill="none" stroke="#1d5ea8" stroke-width="1.5"><path d="M15 4v4M8 12l7-4 7 4v14H8z"/><circle cx="13" cy="18" r="1"/><circle cx="17" cy="21" r="1"/></svg></div>
  <h3 class="display">DRY CLEANING</h3>
  <p>Lorem Ipsum is simply dummy text of the printing and typesetting industry has been the industry's standard dummy.</p>
  <div class="go"><svg width="34" height="12" viewBox="0 0 34 12"><path d="M0 6h32M27 1l5 5-5 5" stroke="#1d5ea8" stroke-width="1.5" fill="none"/></svg></div>
</div>
<div class="abs card" style="left:783px">
  <div class="card-photo" style="background:linear-gradient(135deg,#c9b9a4,#9fb4d6)" role="img" aria-label="Attendant holding garments in a dry cleaning shop"></div>
  <div class="card-badge"><svg width="30" height="30" viewBox="0 0 30 30" fill="none" stroke="#1d5ea8" stroke-width="1.5"><rect x="5" y="6" width="20" height="20" rx="2"/><circle cx="15" cy="17" r="5"/><line x1="5" y1="11" x2="25" y2="11"/></svg></div>
  <h3 class="display">PROFESSIONAL LAUNDRY</h3>
  <p>Lorem Ipsum is simply dummy text of the printing and typesetting industry has been the industry's standard dummy.</p>
  <div class="go"><svg width="34" height="12" viewBox="0 0 34 12"><path d="M0 6h32M27 1l5 5-5 5" stroke="#1d5ea8" stroke-width="1.5" fill="none"/></svg></div>
</div>

<div class="abs pill" style="left:515px;top:2131px;width:170px;padding-left:34px">View More <i><svg width="14" height="14" viewBox="0 0 16 16"><path d="M3 8h10M9 4l4 4-4 4" stroke="#1d5ea8" stroke-width="2" fill="none"/></svg></i></div>

<div class="abs feature" style="left:105px">
  <div class="feature-ring"><svg width="80" height="80" viewBox="0 0 80 80" fill="none" stroke="#1d5ea8" stroke-width="2"><path d="M28 14h24l14 10-6 12-6-3v33H26V33l-6 3-6-12z"/><path d="M34 14l6 10 6-10M40 24v40"/></svg></div>
  <h4 class="display">DRY CLEAN</h4><p>Delivery Available</p>
</div>
<div class="abs feature" style="left:311px">
  <div class="feature-ring"><svg width="80" height="80" viewBox="0 0 80 80" fill="none" stroke="#1d5ea8" stroke-width="2"><path d="M40 10c6 6 14 4 18 8s0 10 6 16-4 12-2 20-12 12-22 14c-10-2-24-6-22-14s-8-14-2-20-2-12 6-16 12-2 18-8z"/><path d="M40 18c5 4 10 3 13 6s0 8 4 12-3 9-1 15-9 9-16 10c-7-1-17-4-16-10s-6-11-1-15-1-8 4-12 8-2 13-6z" stroke-dasharray="3 3"/></svg></div>
  <h4 class="display">LEATHER &amp; SUEDE</h4><p>Please Contact us<br>for Details</p>
</div>
<div class="abs feature" style="left:517px">
  <div class="feature-ring"><svg width="80" height="80" viewBox="0 0 80 80" fill="none" stroke="#1d5ea8" stroke-width="2"><path d="M18 30h44v32H18z M18 46h44 M18 54h44"/><path d="M28 30l12-14 12 14"/></svg></div>
  <h4 class="display">WASH, DRY, FOLD</h4><p>Covid 19 Hours-<br>Open</p>
</div>
<div class="abs feature" style="left:723px">
  <div class="feature-ring"><svg width="90" height="80" viewBox="0 0 90 80" fill="none" stroke="#1d5ea8" stroke-width="2"><rect x="6" y="12" width="38" height="56"/><rect x="46" y="12" width="38" height="56"/><line x1="6" y1="22" x2="84" y2="22"/><circle cx="25" cy="44" r="12"/><circle cx="65" cy="44" r="12"/></svg></div>
  <h4 class="display">OVERSIZE MACHINES</h4><p>7 Days a week<br>8am to 8pm</p>
</div>
<div class="abs feature" style="left:929px">
  <div class="feature-ring"><svg width="80" height="80" viewBox="0 0 80 80" fill="none" stroke="#1d5ea8" stroke-width="2"><rect x="16" y="14" width="34" height="48" rx="2"/><rect x="26" y="10" width="14" height="8"/><circle cx="30" cy="48" r="7"/><rect x="44" y="36" width="20" height="30" rx="2"/><line x1="48" y1="42" x2="60" y2="42"/></svg></div>
  <h4 class="display">COMMERICAL ACCOUNTS</h4><p>Last Wash Begins<br>6:30pm</p>
</div>

<!-- testimonials -->
<h2 class="section-title display" style="top:2640px">OUR CUSTOMERS LOVE<br>OUR SERVICES</h2>

<div class="abs review" style="left:105px">
  <div class="review-avatar" role="img" aria-label="Customer portrait"></div>
  <div class="review-quote">”</div>
  <h5>Marcus Dale</h5><div class="role">Creative Director</div>
  <p>Lorem Ipsum is simply dummy text of the printing and typesetting industry has been the industry's standard.</p>
  <div class="stars">★★★★★</div>
</div>
<div class="abs review" style="left:445px">
  <div class="review-avatar" role="img" aria-label="Customer portrait"></div>
  <div class="review-quote">”</div>
  <h5>Priya Holt</h5><div class="role">Creative Director</div>
  <p>Lorem Ipsum is simply dummy text of the printing and typesetting industry has been the industry's standard.</p>
  <div class="stars">★★★★★</div>
</div>
<div class="abs review" style="left:785px">
  <div class="review-avatar" role="img" aria-label="Customer portrait"></div>
  <div class="review-quote">”</div>
  <h5>Renee K.</h5><div class="role">Creative Director</div>
  <p>Lorem Ipsum is simply dummy text of the printing and typesetting industry has been the industry's standard.</p>
  <div class="stars">★★★★★</div>
</div>
<div class="abs dots"><span></span><span></span><span></span></div>

<!-- quick contact -->
<h2 class="abs qc-title display">QUICK CONTACT</h2>
<div class="abs qc-sub">How Can We Help?</div>
<div class="abs field" style="left:105px;top:3334px;width:167px">Name*</div>
<div class="abs field" style="left:284px;top:3334px;width:136px">Phone*</div>
<div class="abs field" style="left:432px;top:3334px;width:137px">E-Mail*</div>
<div class="abs field" style="left:105px;top:3385px;width:464px;height:96px">Message</div>
<div class="abs send">Send</div>
<div class="abs qc-photo" role="img" aria-label="Red-haired woman in a blue dress beside front-load washers"></div>

<!-- footer -->
<svg class="abs footer-wave" viewBox="0 0 1200 460" preserveAspectRatio="none">
  <path d="M0 42 C200 -10 380 30 560 58 C760 90 980 60 1200 0 L1200 460 L0 460Z" fill="#1e9ad8"/>
  <path d="M0 60 C200 8 380 40 560 70 C760 100 980 72 1200 22 L1200 460 L0 460Z" fill="#1d5ea8"/>
</svg>

<div class="abs f-head" style="left:105px">Map</div>
<div class="abs f-map" role="img" aria-label="Street map showing the laundromat location"></div>
<svg class="abs" style="left:219px;top:3910px" width="14" height="20" viewBox="0 0 14 20"><path d="M7 0a7 7 0 0 1 7 7c0 5-7 13-7 13S0 12 0 7a7 7 0 0 1 7-7z" fill="#1d5ea8"/><circle cx="7" cy="7" r="2.5" fill="#fff"/></svg>

<div class="abs f-head" style="left:438px">Quick Link</div>
<ul class="abs f-links">
  <li>Home</li><li>About us</li><li>Servicese</li><li>Locationse</li><li>Reviewse</li><li>Contact Us</li>
</ul>

<div class="abs f-head" style="left:623px">Contact us</div>
<svg class="abs" style="left:623px;top:3866px" width="10" height="14" viewBox="0 0 14 20"><path d="M7 0a7 7 0 0 1 7 7c0 5-7 13-7 13S0 12 0 7a7 7 0 0 1 7-7z" fill="#1e9ad8"/></svg>
<div class="abs f-text" style="left:647px;top:3858px">Maple Court Shopping Center,<br>2210 Linden Ave NE, # 118,<br>Atlanta, GA 30300</div>
<svg class="abs" style="left:623px;top:3954px" width="12" height="12" viewBox="0 0 24 24" fill="#1e9ad8"><path d="M6.6 10.8a15 15 0 0 0 6.6 6.6l2.2-2.2c.3-.3.7-.4 1-.2 1.1.4 2.3.6 3.6.6.6 0 1 .4 1 1V20c0 .6-.4 1-1 1A17 17 0 0 1 3 4c0-.6.4-1 1-1h3.5c.6 0 1 .4 1 1 0 1.3.2 2.5.6 3.6.1.3 0 .7-.2 1z"/></svg>
<div class="abs f-text" style="left:647px;top:3949px">(404) 555-0182</div>
<svg class="abs" style="left:623px;top:3999px" width="12" height="10" viewBox="0 0 12 10"><rect width="12" height="10" fill="#1e9ad8"/></svg>
<div class="abs f-text" style="left:647px;top:3993px">hello@sudsharbor-example.com</div>

<div class="abs f-head" style="left:898px">Newsletter</div>
<div class="abs f-text" style="left:898px;top:3856px;width:200px;font-size:11px">Join Our Newsletter to receive the latest update and promotion.</div>
<div class="abs f-input">Your Email</div>
<div class="abs f-btn">Subscribe</div>

<div class="abs copyright">Copyright © 2021 <b>Suds Harbor</b>, All Rights Reserved.</div>
<div class="abs social" style="left:925px"></div>
<div class="abs social" style="left:970px"></div>
<div class="abs social" style="left:1015px"></div>
<div class="abs social" style="left:1060px"></div>

</body>
</html>
```